Compelling Home Page for Clip Harbor Partners

We are a Video SEO specialist that get websites on top of the front page of Zentrova and FlickBarn with video thumbprints that generate great traffic. Video SEO is all we do

see what we're offering at a salespage www.plumfieldreels.example. However, please omit "guarantee"

he home page should introduce our company as a premier company for helping brands get their videos on the front page of zentrova and high up in flickbarn. Should incorporate video "thumbnails" as part of the design. These could be the "triangular click buttons" or little video screens you see as "thumbnails" Needs a prominent place for a video about videoSEO. on Left side of page towards the top.

Needs buttons across the top for other pages. See www.brastonclips.example for frame of reference we want to be better than them.

Must incorporate our logo. We'd like to see the logo on dark background as well as white background.

Simple but with bright and vibrant highlights that look sophisticated, cutting edge and accountable. Shows credentials. Links with examples of thumbnails that are on the front page

We want to beat www.brastonclips.example check it out for point of reference

Target Market(s)

large corporations who have videos already and want to get better traction. Marlow 500. Advertising Agencies for Marlow 500's

Requirements
Must have
• Incorporate our logo. clean, easy to read

```html
<!DOCTYPE html>
<html lang="en">
<head>
<meta charset="utf-8">
<title>Clip Harbor Partners – Video SEO</title>
<link href="https://fonts.googleapis.com/css2?family=Fenix&family=Alegreya:ital@0;1&family=Lato:wght@400&family=Nothing+You+Could+Do&display=swap" rel="stylesheet">
<style>
:root{
  --black:#000;
  --white:#fff;
  --orange:#f26b10;
  --orange-dark:#c94a00;
  --orange-light:#ff9a3a;
  --gold:#f7b500;
  --blue:#2a8fcf;
  --text:#222;
  --grey:#555;
  --rule:#bbb;
  --navy:#0d1622;
  --green:#3aa63a;
  --person:#e25a10;
}
*{margin:0;padding:0;box-sizing:border-box}
html,body{width:961px;height:1200px;overflow:hidden;background:var(--white)}
body{position:relative;font-family:Arial,Helvetica,sans-serif;color:var(--text)}
.abs{position:absolute}

/* header */
.site-header{position:absolute;left:0;top:0;width:961px;height:66px;background:var(--black)}
.brand{position:absolute;left:122px;top:6px;display:flex;align-items:center;gap:12px}
.brand-dot{width:54px;height:54px;border-radius:50%;background:var(--orange)}
.brand-name{font-family:'Lato',sans-serif;font-size:28px;color:var(--white)}
.main-nav a{position:absolute;top:24px;font-family:'Lato',sans-serif;font-size:14px;color:var(--white);text-decoration:none}
.main-nav a.is-active{top:21px;left:501px;width:59px;height:24px;line-height:24px;text-align:center;background:var(--gold);color:#222;border-radius:2px}

/* hero */
.hero-title{left:0;top:78px;width:961px;text-align:center;font-family:'Fenix',serif;font-size:37px;color:#111}
.hero-sub{left:0;top:121px;width:961px;text-align:center;font-family:'Lato',sans-serif;font-size:15px;line-height:21px;color:var(--grey)}
.hero-sub em{font-family:'Alegreya',serif;color:var(--orange)}
.hero-video{left:78px;top:178px;width:452px;height:278px;border-radius:10px 10px 30px 30px;background:linear-gradient(#d9d9d9,#a9a9a9)}
.hero-video .screen{position:absolute;left:62px;top:12px;width:328px;height:196px;background:#050505;border-radius:2px}
.cta{display:flex;align-items:center;justify-content:space-between;padding:0 12px 0 10px;background:linear-gradient(var(--orange-light),var(--orange) 55%,var(--orange-dark));border:1px solid #b84300;border-radius:3px;color:var(--white);font-family:'Alegreya',serif;font-style:italic;font-size:18px}
.cta-arrow{width:22px;height:22px;border-radius:50%;background:#5a2a0a;color:var(--white);font-style:normal;font-size:13px;text-align:center;line-height:22px}
.hero-cta{left:154px;top:462px;width:299px;height:37px}
.benefit{font-family:'Nothing You Could Do',cursive;font-size:22px;color:#111}
.engine{font-family:'Lato',sans-serif;font-size:20px}

/* band */
.seo-band{left:0;top:523px;width:961px;height:127px;background:var(--black)}
.seo-band h2{position:absolute;left:0;top:10px;width:961px;text-align:center;font-family:'Fenix',serif;font-weight:400;font-size:23px;color:var(--orange)}
.pull{position:absolute;top:60px;font-family:'Alegreya',serif;font-size:15px;line-height:20px;color:var(--white)}
.pull::before{content:"\201C";position:absolute;left:-25px;top:-6px;font-size:26px}

/* intro */
.intro-title{left:95px;top:676px;width:370px;font-family:'Fenix',serif;font-weight:400;font-size:24px;line-height:29px;color:#111}
.accent{color:var(--blue)}
.intro-copy{left:97px;top:780px;width:372px;font-size:12px;line-height:19.2px;color:#333}
.why-title{left:101px;top:952px;font-family:'Fenix',serif;font-weight:400;font-size:24px;line-height:24px;color:#111}
.reason{position:absolute;left:104px;display:flex;align-items:center;gap:10px}
.reason .num{font-family:'Nothing You Could Do',cursive;font-size:20px;width:24px}
.reason span.txt{font-family:'Alegreya',serif;font-style:italic;font-size:13px;color:var(--blue)}
.divider{left:480px;top:682px;width:1px;height:390px;background:var(--rule)}

/* proof */
.proof-title{left:495px;top:675px;font-family:'Alegreya',serif;font-style:italic;font-size:22px;color:#111}
.clients{left:518px;top:720px;width:320px;height:84px}
.client{position:absolute;font-family:'Lato',sans-serif;font-size:10px;color:#444;display:flex;align-items:center;gap:3px}
.client i{display:inline-block;width:7px;height:7px;background:#999}
.aside-line{font-family:'Alegreya',serif;font-style:italic;font-size:20px;color:#111}
.testimonial-mark{left:514px;top:852px;font-family:'Alegreya',serif;font-size:44px;color:var(--blue)}
.testimonial{left:553px;top:862px;width:270px;font-family:'Alegreya',serif;font-style:italic;font-size:18px;line-height:22px;color:#111}
.cite{left:700px;top:941px;width:148px;text-align:right;font-size:11px;line-height:14px}
.cite a{color:var(--blue);text-decoration:none}
.profit-cta{left:541px;top:1030px;width:252px;height:37px}

/* footer */
.site-footer{left:0;top:1123px;width:961px;height:77px;background:linear-gradient(#1b2636,var(--navy));color:var(--white);text-align:center;font-size:10.5px;line-height:15px;padding-top:14px}
</style>
</head>
<body>

<header class="site-header">
  <div class="brand"><span class="brand-dot"></span><span class="brand-name">Clip Harbor Partners</span></div>
  <nav class="main-nav">
    <a class="is-active" href="#">Home</a>
    <a href="#" style="left:573px">Services</a>
    <a href="#" style="left:643px">Examples</a>
    <a href="#" style="left:722px">Order</a>
    <a href="#" style="left:779px">Contact Us</a>
  </nav>
</header>

<h1 class="abs hero-title" style="font-weight:400">Build More Traffic, Leads, and Sales to Your Site</h1>
<p class="abs hero-sub">No matter what you sell or what your company size, <em>Video Marketing</em> is very likely your best<br>opportunity to dramatically increase online sales this year:</p>

<div class="abs hero-video" role="img" aria-label="Laptop showing the featured Video SEO introduction video">
  <div class="screen"></div>
</div>
<a class="abs cta hero-cta" href="#">Get your videos to the top today! <span class="cta-arrow">&#10095;</span></a>

<svg class="abs" style="left:505px;top:200px" width="120" height="290" viewBox="0 0 120 290" fill="none" stroke="#333" stroke-width="1">
  <path d="M6 40 Q50 24 95 15"/><path d="M85 11 L97 14 L88 21"/>
  <path d="M10 79 Q60 70 102 66"/><path d="M92 61 L104 66 L92 71"/>
  <path d="M28 117 Q80 118 122 123"/>
  <path d="M18 147 Q65 158 108 170"/><path d="M97 162 L109 170 L96 172"/>
  <path d="M110 271 Q70 272 16 276"/><path d="M28 270 L14 276 L28 281"/>
</svg>
<svg class="abs" style="left:612px;top:315px" width="20" height="16" viewBox="0 0 20 16" fill="none" stroke="#333"><path d="M0 8 L18 8 M11 3 L18 8 L11 13"/></svg>

<div class="abs" style="left:618px;top:190px;font:700 34px 'Lato',sans-serif;color:var(--green)">$</div>
<span class="abs benefit" style="left:662px;top:180px;transform:rotate(-4deg)">Increase Online Sales</span>
<svg class="abs" style="left:637px;top:246px" width="38" height="34" viewBox="0 0 38 34"><circle cx="19" cy="10" r="9" fill="var(--person)"/><path d="M2 34 Q2 20 19 20 Q36 20 36 34Z" fill="var(--person)"/></svg>
<span class="abs benefit" style="left:700px;top:236px;transform:rotate(-4deg)">Gain Traffic</span>
<svg class="abs" style="left:652px;top:306px" width="38" height="29" viewBox="0 0 38 29"><rect x="1" y="1" width="36" height="27" fill="none" stroke="var(--blue)" stroke-width="2"/><rect x="5" y="6" width="14" height="3" fill="var(--blue)"/><rect x="5" y="12" width="14" height="3" fill="var(--blue)"/><rect x="5" y="18" width="14" height="3" fill="var(--blue)"/><rect x="22" y="8" width="11" height="14" fill="var(--blue)"/></svg>
<span class="abs benefit" style="left:706px;top:312px;transform:rotate(3deg)">Generate Leads</span>
<span class="abs benefit" style="left:637px;top:363px;transform:rotate(3deg)">Get to the top of...</span>
<span class="abs engine" style="left:650px;top:419px;color:#333">FlickBarn</span>
<span class="abs engine" style="left:735px;top:428px;color:var(--blue)">Zentrova</span>
<span class="abs engine" style="left:668px;top:463px;color:var(--blue)">Searvio</span>

<section class="abs seo-band">
  <h2>Video SEO is the next step...</h2>
  <p class="pull" style="left:107px">Video is the next search<br>engine frontier ...</p>
  <p class="pull" style="left:317px">Video puts your sales<br>process on auto-pilot ...</p>
  <p class="pull" style="left:518px">Video harnesses the<br>&nbsp;power of sight and sound ...</p>
  <p class="pull" style="left:737px">Video marketing is an<br>&nbsp;emerging media ...</p>
</section>

<h2 class="abs intro-title"><span class="accent">Clip Harbor Partners</span> helps brands get their videos on the front page of zentrova and high up in flickbarn.</h2>
<p class="abs intro-copy">You'll get first page Zentrova video listings or you get your money back! We work with ALL types of products and services at reasonable rates...We help entrepreneurs, small businesses, and even large brands (affiliate marketers too)...Plus, WE can produce the videos for you--OR--work with video's YOU provide us. Our SERVICE fees are always bid on a flat-rate project basis. We start with projects as simple as an effective about-us video, and go all the way through large branding based campaigns targeting millions of visitors</p>
<h2 class="abs why-title">Why us <span class="accent">VIDEO</span> is to Expand Your<br>TRAFFIC and SALES</h2>
<div class="reason" style="top:1020px"><svg width="34" height="10" viewBox="0 0 34 10" fill="none" stroke="#222"><path d="M1 5 L32 5 M25 1 L32 5 L25 9"/></svg><span class="num">1</span><span class="txt">Less Competition in the VIDEO Keyword Space</span></div>
<div class="reason" style="top:1050px"><svg width="34" height="10" viewBox="0 0 34 10" fill="none" stroke="#222"><path d="M1 5 L32 5 M25 1 L32 5 L25 9"/></svg><span class="num">2</span><span class="txt">The SIZE of the Opportunity is Astounding</span></div>

<div class="abs divider"></div>

<h2 class="abs proof-title" style="font-weight:400">Companies love <span class="accent">Our Work</span></h2>
<div class="abs clients">
  <span class="client" style="left:4px;top:8px"><i></i>Norbeck</span>
  <span class="client" style="left:84px;top:8px"><i></i>Tallow Grain</span>
  <span class="client" style="left:150px;top:8px"><i></i>Veltro</span>
  <span class="client" style="left:226px;top:8px"><i></i>Ember Stack</span>
  <span class="client" style="left:275px;top:22px"><i></i>Crestline Pay</span>
  <span class="client" style="left:4px;top:48px"><i></i>Orbit Pay</span>
  <span class="client" style="left:86px;top:44px"><i></i>Petralon</span>
  <span class="client" style="left:146px;top:36px"><i></i>Swirlhaus</span>
  <span class="client" style="left:120px;top:66px"><i></i>Keepsake Co</span>
  <span class="client" style="left:216px;top:52px"><i></i>Leafworth</span>
  <span class="client" style="left:283px;top:50px"><i></i>Torvane</span>
</div>
<p class="abs aside-line" style="left:497px;top:813px">... so do individuals</p>
<span class="abs testimonial-mark">&ldquo;</span>
<p class="abs testimonial">&nbsp;&nbsp;... We also now occupy 6 out of 7 of the first places in Zentrova. [...] just do it before they get too busy.</p>
<p class="abs cite">Dorian Keswick,<br><a href="#">voltmarket.example</a></p>
<p class="abs aside-line" style="left:495px;top:978px">... and you will to!</p>
<a class="abs cta profit-cta" href="#">start earning profits today! <span class="cta-arrow">&#10095;</span></a>

<footer class="abs site-footer">
  &copy; Plumfield Reels.com, LLC. - All Rights Reserved<br>
  Trademarks on this page are the property of their respective owners.
</footer>

</body>
</html>
```